New Business Card Design

We would like to refresh our business cards and make them look better. We are an IT company specialising in Cloud Services, IT Managed Services, software and hardware. I have attached a PSD of our current design. Also attached our logo.
Updates

I have uploaded all new logos in EPS format.

Can you please edit all designs to include a job title for Marcus Hale, eg. General Manager

Industry/Entity Type

Software

Colors
ffffff

Requirements
Must have
• Please use white background.
Should not have
• Black background

```html
<!DOCTYPE html>
<html lang="en">
<head>
<meta charset="utf-8">
<title>Northgate Technology – Business Cards</title>
<link href="https://fonts.googleapis.com/css2?family=Open+Sans:wght@400;600;700&display=swap" rel="stylesheet">
<style>
  :root {
    --page: #eceae6;
    --card: #ffffff;
    --band: #8c97a3;
    --accent: #c0392b;
    --ink: #1f2a33;
    --text: #3a3f44;
  }
  * { box-sizing: border-box; margin: 0; padding: 0; }
  html, body { width: 1200px; height: 720px; overflow: hidden; }
  body {
    background: var(--page);
    font-family: "Open Sans", Arial, sans-serif;
    display: flex;
    align-items: center;
    justify-content: center;
    gap: 40px;
  }
  .card {
    position: relative;
    width: 540px;
    height: 320px;
    background: var(--card);
    box-shadow: 0 2px 10px rgba(0,0,0,.12);
    overflow: hidden;
  }

  /* Front */
  .card-front .side-band {
    position: absolute; left: 0; top: 0; bottom: 0;
    width: 110px;
    background: var(--band);
  }
  .card-front .band-tab {
    position: absolute; left: 34px; top: 44px;
    width: 110px; height: 80px;
    background: var(--card);
    border-radius: 0 0 0 24px;
  }
  .card-front .accent-rule {
    position: absolute; left: 128px; top: 70px; bottom: 0;
    width: 2px; background: var(--accent);
  }
  .brand-name {
    font-weight: 400;
    color: var(--ink);
    letter-spacing: .02em;
    line-height: 1.15;
  }
  .card-front .brand-name {
    position: absolute; left: 160px; top: 38px;
    font-size: 26px;
  }
  .person {
    position: absolute; right: 32px; top: 118px;
    text-align: right;
  }
  .person-name { color: var(--accent); font-weight: 700; font-size: 16px; }
  .person-role { color: var(--ink); font-size: 11.5px; margin-top: 1px; }
  .contact-list {
    position: absolute; left: 148px; bottom: 40px;
    list-style: none;
  }
  .contact-list li {
    display: flex; align-items: center; gap: 7px;
    font-size: 12.5px; color: var(--text);
    line-height: 21px;
  }
  .contact-icon { width: 12px; height: 12px; flex: none; }

  /* Back */
  .card-back {
    display: flex; flex-direction: column;
    align-items: center; justify-content: center;
  }
  .card-back .brand-name {
    font-size: 44px;
    text-align: center;
    margin-top: -10px;
  }
  .tagline {
    margin-top: 48px;
    text-align: center;
    font-size: 15px;
    line-height: 1.5;
    color: var(--text);
  }
</style>
</head>
<body>

  <section class="card card-front" aria-label="Business card front">
    <div class="side-band"></div>
    <div class="band-tab"></div>
    <div class="accent-rule"></div>
    <p class="brand-name">Northgate Technology</p>
    <div class="person">
      <p class="person-name">Marcus Hale</p>
      <p class="person-role">General Manager</p>
    </div>
    <ul class="contact-list">
      <li>
        <svg class="contact-icon" viewBox="0 0 12 12" aria-hidden="true"><circle cx="6" cy="6" r="6" fill="#c0392b"/><path d="M4 3.2c.4-.3.8 0 1 .5l.3.8c.1.3-.1.5-.3.7.3.7.8 1.2 1.5 1.5.2-.2.4-.4.7-.3l.8.3c.5.2.8.6.5 1-.4.6-1 .8-1.7.5C5.3 7.6 4.3 6.6 3.8 5.2c-.3-.7-.2-1.5.2-2z" fill="#fff"/></svg>
        07 3555 0142
      </li>
      <li>
        <svg class="contact-icon" viewBox="0 0 12 12" aria-hidden="true"><circle cx="6" cy="6" r="6" fill="#c0392b"/><rect x="4" y="2.5" width="4" height="7" rx=".8" fill="#fff"/><rect x="4.7" y="3.4" width="2.6" height="4" fill="#c0392b"/></svg>
        0491 570 156
      </li>
      <li>
        <svg class="contact-icon" viewBox="0 0 12 12" aria-hidden="true"><circle cx="6" cy="6" r="6" fill="#c0392b"/><rect x="2.8" y="3.8" width="6.4" height="4.4" fill="#fff"/><path d="M2.8 3.8L6 6.3l3.2-2.5" fill="none" stroke="#c0392b" stroke-width=".7"/></svg>
        mhale@northgateit.com.au
      </li>
      <li>
        <svg class="contact-icon" viewBox="0 0 12 12" aria-hidden="true"><circle cx="6" cy="6" r="6" fill="#c0392b"/><circle cx="6" cy="6" r="3.3" fill="none" stroke="#fff" stroke-width=".8"/><ellipse cx="6" cy="6" rx="1.4" ry="3.3" fill="none" stroke="#fff" stroke-width=".7"/><path d="M2.7 6h6.6" stroke="#fff" stroke-width=".7"/></svg>
        www.northgateit.com.au
      </li>
    </ul>
  </section>

  <section class="card card-back" aria-label="Business card back">
    <p class="brand-name">Northgate<br>Technology</p>
    <p class="tagline">We are an IT company specializing in Cloud Services<br>IT Managed Services, software and hardware</p>
  </section>

</body>
</html>
```